New Web Design Project for kids music school

We need a homepage mockup for a kids' music program. Use your creative talent to come up with something visually appeal and professional for this web-site.

More information is provided in the PDF file called HOME. Also included in this file are links to the photos to be used.

Please let me know if you have more questions.

Target Market(s)

parents

Number of Pages Required

1 page

Font styles to use
Sans Serif

```html
<!DOCTYPE html>
<html lang="en">
<head>
<meta charset="utf-8">
<title>Little Notes! — Live Music Education for Kids</title>
<link rel="stylesheet" href="https://fonts.googleapis.com/css2?family=Kurale&family=Lato:wght@300;400;700&display=swap">
<style>
:root{
  --blue:#0d0dc4;
  --blue-dark:#0a0a9e;
  --yellow:#fcff2a;
  --lavender:#bdbaf2;
  --lavender-soft:#dcdaf8;
  --ink:#222230;
  --muted:#555566;
  --footer-bg:#f5f5f8;
  --white:#ffffff;
}
*{box-sizing:border-box;margin:0;padding:0}
html,body{width:1200px;height:2819px;overflow:hidden;background:var(--white)}
body{position:relative;font-family:'Lato',sans-serif;color:var(--ink)}
.abs{position:absolute}
.serif{font-family:'Kurale',serif;font-weight:400}

/* header */
.site-header{left:0;top:0;width:1200px;height:82px;background:var(--white)}
.brand{left:156px;top:20px;font-family:'Kurale',serif;font-size:28px;line-height:1;color:var(--blue)}
.nav{top:37px;font-size:13px;font-weight:700;letter-spacing:.3px;color:var(--ink)}
.nav.active{color:var(--blue)}
.call-btn{left:871px;top:21px;width:184px;height:49px;border-radius:25px;background:var(--blue);color:var(--white);font-size:14px;font-weight:700;display:flex;align-items:center;justify-content:center;gap:10px}

/* hero */
.hero{left:0;top:82px;width:1200px;height:453px;background:linear-gradient(100deg,#6a7f58 0%,#b3a07e 30%,#d98aa3 55%,#c9b7a9 75%,#9c8c8a 100%)}
.hero-shade{left:0;top:82px;width:1200px;height:453px;background:linear-gradient(90deg,rgba(0,0,0,.35),rgba(0,0,0,.05) 65%)}
.badge{left:145px;top:179px;height:36px;padding:0 18px;border-radius:6px;background:var(--blue);color:var(--white);font-size:16px;line-height:36px}
.hero-title{left:148px;top:232px;font-size:40px;line-height:50px;color:var(--white);text-shadow:0 2px 6px rgba(0,0,0,.4)}
.hero-sub{left:150px;top:339px;font-size:16px;color:var(--white)}
.btn{display:flex;align-items:center;justify-content:center;border-radius:22px;font-family:'Kurale',serif;font-size:15px}
.btn-yellow{background:var(--yellow);color:var(--blue)}
.btn-blue{background:var(--blue);color:var(--white)}
.btn-ring{border:1px solid #d8d8e2;border-radius:27px;background:var(--white)}

/* photo placeholders */
.photo{position:absolute}
.frame-blue{background:var(--blue)}
.frame-yellow{background:var(--yellow)}
.deco{position:absolute;border-radius:50%;background:var(--lavender-soft)}

.sec-title{font-size:30px;color:var(--ink)}
.sec-sub{font-size:16px;color:var(--blue)}
.sec-body{font-size:14px;line-height:28px;color:var(--muted);font-weight:300}

/* virtual band */
.virtual{left:0;top:1637px;width:1040px;height:353px;background:linear-gradient(100deg,#4f4fd8,#3e3ed0 60%,#3434c4);border-bottom-right-radius:150px;border-top:6px solid var(--yellow)}
.virtual-title{left:540px;top:1752px;width:406px;text-align:center;font-size:35px;color:var(--white)}
.virtual-sub{left:540px;top:1806px;width:406px;text-align:center;font-size:15px;color:var(--white)}

.h2{width:1200px;text-align:center;font-size:30px;letter-spacing:1.5px;color:var(--ink)}
.video{position:absolute;top:2103px;width:284px;height:237px;background:linear-gradient(160deg,#8a7a6a,#5a4e48 60%,#3a3436)}
.play{position:absolute;width:38px;height:38px;border-radius:50%;background:var(--white);display:flex;align-items:center;justify-content:center}
.video-label{position:absolute;font-size:13px;color:var(--white);white-space:nowrap}
.all-videos{left:459px;top:2293px;width:284px;height:47px;background:var(--blue);color:var(--white);font-size:16px;display:flex;align-items:center;justify-content:center}

.insta{position:absolute;top:2447px;width:195px;height:178px}

.footer{left:0;top:2625px;width:1200px;height:194px;background:var(--footer-bg)}
.divider{position:absolute;top:2668px;width:1px;height:92px;background:#dcdce4}
.foot-small{font-size:9px;color:var(--ink)}
.foot-text{font-size:13px;line-height:21px;color:var(--ink)}
.social{position:absolute;top:2686px;width:20px;height:20px;border-radius:3px}
</style>
</head>
<body>

<header class="abs site-header">
  <div class="abs brand">Little<br>Notes!</div>
  <a class="abs nav active" style="left:579px">HOME</a>
  <a class="abs nav" style="left:660px">PROGRAMS
    <svg width="10" height="7" viewBox="0 0 10 7" style="margin-left:10px"><path d="M1 1l4 4 4-4" stroke="#222230" stroke-width="1.4" fill="none"/></svg></a>
  <a class="abs nav" style="left:782px">CONTACT</a>
  <a class="abs call-btn">
    <svg width="16" height="16" viewBox="0 0 24 24" fill="none" stroke="#fff" stroke-width="2"><path d="M22 16.9v3a2 2 0 0 1-2.2 2 19.8 19.8 0 0 1-8.6-3.1 19.5 19.5 0 0 1-6-6A19.8 19.8 0 0 1 2.1 4.2 2 2 0 0 1 4.1 2h3a2 2 0 0 1 2 1.7c.1 1 .4 1.9.7 2.8a2 2 0 0 1-.5 2.1L8 9.9a16 16 0 0 0 6 6l1.3-1.3a2 2 0 0 1 2.1-.5c.9.3 1.8.6 2.8.7a2 2 0 0 1 1.8 2z"/></svg>
    (555) 210-4477</a>
</header>

<section>
  <div class="abs hero" role="img" aria-label="Photo of cheerful young children sitting on a classroom floor raising their hands"></div>
  <div class="abs hero-shade"></div>
  <div class="abs badge">Welcome to Little Notes!</div>
  <h1 class="abs hero-title serif">Live Music Education &amp; The Stars!<br>Performing Program</h1>
  <p class="abs hero-sub">Programs available for kids 3 months to 14 years old</p>
  <a class="abs btn btn-yellow" style="left:162px;top:397px;width:148px;height:38px">Learn More</a>
</section>

<section>
  <div class="abs frame-blue" style="left:33px;top:568px;width:138px;height:138px"></div>
  <div class="photo" style="left:47px;top:580px;width:334px;height:333px;background:linear-gradient(135deg,#a8a7a2,#8c8a84 60%,#6f8fc0)" role="img" aria-label="Photo of a toddler playing a hand drum"></div>
  <div class="abs" style="left:404px;top:762px;width:150px;height:146px;border:4px solid var(--lavender);border-left:none;border-bottom:none;border-top-right-radius:40px"></div>
  <div class="photo" style="left:404px;top:768px;width:143px;height:140px;background:linear-gradient(135deg,#c98a86,#8a9ab8)" role="img" aria-label="Photo of children playing with instruments on a table"></div>
  <div class="abs" style="left:232px;top:937px;width:150px;height:146px;border:4px solid var(--lavender);border-right:none;border-top:none;border-bottom-left-radius:40px"></div>
  <div class="photo" style="left:238px;top:937px;width:144px;height:140px;background:linear-gradient(135deg,#9aa87a,#d68aa6)" role="img" aria-label="Photo of excited girls in a music class"></div>
  <div class="photo" style="left:402px;top:937px;width:145px;height:140px;background:linear-gradient(135deg,#9cb48a,#7c8c6c)" role="img" aria-label="Photo of toddlers dancing in a classroom"></div>

  <div class="deco" style="left:135px;top:985px;width:58px;height:58px" role="img" aria-label="Decorative drum icon"></div>
  <div class="deco" style="left:948px;top:578px;width:58px;height:52px" role="img" aria-label="Decorative music staff icon"></div>
  <div class="deco" style="left:822px;top:932px;width:74px;height:76px" role="img" aria-label="Decorative guitar with notes icon"></div>

  <h2 class="abs sec-title serif" style="left:598px;top:660px">Live Music Program</h2>
  <p class="abs sec-sub" style="left:602px;top:719px">Infant/Toddler Music (ages 3 months - 3.5 years)</p>
  <p class="abs sec-body" style="left:602px;top:758px;width:430px">This “mommy &amp; me” style class is a 45 minute live music adventure. Each class has a singer and pianist guiding little ones through 3 boxes of instruments built for their little hands. We use music to teach movement, vocabulary, numbers, letters, confidence and build a love of music.</p>
  <div class="abs btn-ring" style="left:605px;top:923px;width:172px;height:52px"></div>
  <a class="abs btn btn-blue" style="left:617px;top:929px;width:149px;height:40px">Learn More</a>
</section>

<section>
  <div class="abs frame-yellow" style="left:990px;top:1046px;width:140px;height:140px"></div>
  <div class="photo" style="left:784px;top:1061px;width:334px;height:334px;background:radial-gradient(circle at 55% 50%,#6a4a3a,#1a1212 65%,#000)" role="img" aria-label="Photo of young performers posing on a dark stage"></div>
  <div class="abs" style="left:610px;top:1244px;width:152px;height:146px;border:5px solid var(--yellow);border-right:none;border-bottom:none;border-top-left-radius:40px"></div>
  <div class="photo" style="left:618px;top:1250px;width:144px;height:140px;background:radial-gradient(circle,#7a5a6a,#111 70%)" role="img" aria-label="Photo of three girls acting on stage"></div>
  <div class="photo" style="left:618px;top:1419px;width:145px;height:139px;background:linear-gradient(135deg,#b6b0a6,#d9aeb4)" role="img" aria-label="Photo of a smiling toddler with a bow"></div>
  <div class="abs" style="left:790px;top:1419px;width:144px;height:146px;border:5px solid var(--yellow);border-left:none;border-top:none;border-bottom-right-radius:40px"></div>
  <div class="photo" style="left:783px;top:1419px;width:144px;height:139px;background:radial-gradient(circle,#6a5a5a,#141010 70%)" role="img" aria-label="Photo of a stage scene with children in costume"></div>

  <div class="deco" style="left:547px;top:1137px;width:56px;height:56px" role="img" aria-label="Decorative music notes icon"></div>
  <div class="deco" style="left:1008px;top:1443px;width:66px;height:66px" role="img" aria-label="Decorative trumpet icon"></div>
  <div class="deco" style="left:98px;top:1494px;width:46px;height:50px" role="img" aria-label="Decorative saxophone icon"></div>

  <h2 class="abs sec-title serif" style="left:150px;top:1244px;width:404px;text-align:right">STARS! Performance Program</h2>
  <p class="abs sec-sub" style="left:150px;top:1300px;width:404px;text-align:right">Infant/Toddler Music (ages 3 months - 3.5 years)</p>
  <p class="abs sec-body" style="left:150px;top:1346px;width:404px;text-align:right">Kids work once a week to put on a show customized for their class. Every child has a solo, lines, and a big part. We have classes for kids ages 3-14. Our mission is confidence and teaching important life skills through theater. All classes perform their show at the end of the session</p>
  <div class="abs btn-ring" style="left:383px;top:1510px;width:172px;height:52px"></div>
  <a class="abs btn btn-blue" style="left:395px;top:1516px;width:149px;height:40px">Learn More</a>
</section>

<section>
  <div class="abs virtual" role="img" aria-label="Photo of children dancing in a classroom under a blue tint"></div>
  <h2 class="abs virtual-title serif">Virtual Music Lessons</h2>
  <p class="abs virtual-sub">We’re now offering one on one virtual music lessons</p>
  <div class="abs" style="left:591px;top:1857px;width:172px;height:52px;border:1px solid rgba(255,255,255,.6);border-radius:27px"></div>
  <a class="abs btn btn-yellow" style="left:603px;top:1863px;width:149px;height:40px">Learn More</a>
  <div class="deco" style="left:1072px;top:1738px;width:92px;height:98px" role="img" aria-label="Decorative guitar with notes icon"></div>
</section>

<section>
  <h2 class="abs h2 serif" style="left:0;top:2034px">Our Latest Video</h2>

  <div class="video" style="left:153px" role="img" aria-label="Video still of a teacher leading a movement class">
    <div class="play" style="left:16px;top:147px"><svg width="12" height="12" viewBox="0 0 12 12"><path d="M2 1l9 5-9 5z" fill="#e02020"/></svg></div>
    <div class="video-label" style="left:18px;top:203px">Live Music class! Shake, drum, swish!</div>
  </div>

  <div class="video" style="left:459px;height:177px" role="img" aria-label="Video still of a teacher reading a picture book">
    <div class="play" style="left:15px;top:95px"><svg width="12" height="12" viewBox="0 0 12 12"><path d="M2 1l9 5-9 5z" fill="#e02020"/></svg></div>
    <div class="video-label" style="left:15px;top:150px">Musical Story Time: SNOW CASTLE</div>
  </div>
  <a class="abs all-videos">Video All Videos</a>

  <div class="video" style="left:762px" role="img" aria-label="Video still of a teacher presenting a storybook">
    <div class="play" style="left:19px;top:150px"><svg width="12" height="12" viewBox="0 0 12 12"><path d="M2 1l9 5-9 5z" fill="#e02020"/></svg></div>
    <div class="video-label" style="left:21px;top:205px">Day 4: Pirate Island Live Musical Story</div>
  </div>
</section>

<section>
  <h2 class="abs h2 serif" style="left:0;top:2376px">Follows On Instagram</h2>
  <div class="insta" style="left:0;background:linear-gradient(135deg,#c9a48a,#7a8aa0)" role="img" aria-label="Photo of teachers holding a book"></div>
  <div class="insta" style="left:200px;background:linear-gradient(135deg,#9a7a5a,#d6a0b0)" role="img" aria-label="Photo of a child in a costume on the floor"></div>
  <div class="insta" style="left:400px;background:linear-gradient(135deg,#555,#1e1e1e)" role="img" aria-label="Black and white photo of a child with headphones"></div>
  <div class="insta" style="left:599px;background:linear-gradient(135deg,#5a5ad8,#4040c0)" role="img" aria-label="Photo of a girl dancing under a blue tint">
    <div style="position:absolute;left:88px;top:80px;width:26px;height:26px;border:2px solid #fff;border-radius:6px"></div>
    <div style="position:absolute;left:0;top:115px;width:195px;text-align:center;font-size:13px;color:#fff">Follow Us</div>
  </div>
  <div class="insta" style="left:799px;background:radial-gradient(circle,#6a5050,#141010 70%)" role="img" aria-label="Photo of a holiday stage performance"></div>
  <div class="insta" style="left:999px;width:201px;background:linear-gradient(135deg,#c9a890,#8a4a6a)" role="img" aria-label="Photo of a child watching a lesson on a tablet"></div>
</section>

<footer class="abs footer"></footer>
<div class="abs brand" style="left:158px;top:2685px;font-size:24px">Little<br>Notes!</div>
<p class="abs foot-small" style="left:165px;top:2746px">Copyright © 2020 Little Notes!</p>
<p class="abs foot-small" style="left:165px;top:2766px">All rights reserved.</p>

<div class="divider" style="left:342px"></div>
<div class="divider" style="left:611px"></div>
<div class="divider" style="left:912px"></div>

<svg class="abs" style="left:377px;top:2686px" width="13" height="16" viewBox="0 0 24 30"><path d="M12 0a10 10 0 0 0-10 10c0 8 10 20 10 20s10-12 10-20A10 10 0 0 0 12 0zm0 14a4 4 0 1 1 0-8 4 4 0 0 1 0 8z" fill="#222230"/></svg>
<p class="abs foot-text" style="left:402px;top:2684px;font-weight:700;font-size:12px">ADDRESS</p>
<p class="abs foot-text" style="left:400px;top:2710px">42 Maple Grove Rd. Brookfield,<br>MA 01506</p>

<svg class="abs" style="left:664px;top:2690px" width="14" height="14" viewBox="0 0 24 24"><path d="M22 16.9v3a2 2 0 0 1-2.2 2A19.8 19.8 0 0 1 2.1 4.2 2 2 0 0 1 4.1 2h3a2 2 0 0 1 2 1.7l.7 2.8-2 2.4a16 16 0 0 0 7.3 7.3l2.4-2 2.8.7a2 2 0 0 1 1.7 2z" fill="#222230"/></svg>
<p class="abs foot-text" style="left:703px;top:2686px">(555) 210-4477</p>
<svg class="abs" style="left:664px;top:2723px" width="16" height="12" viewBox="0 0 16 12"><rect width="16" height="12" rx="1" fill="#222230"/><path d="M1 1l7 5 7-5" stroke="#f5f5f8" stroke-width="1.3" fill="none"/></svg>
<p class="abs foot-text" style="left:703px;top:2718px">hello@littlenotesmusic.com</p>

<div class="social" style="left:954px;background:#3b5998" aria-label="Social profile"></div>
<div class="social" style="left:987px;background:#2ea6e0" aria-label="Social profile"></div>
<div class="social" style="left:1020px;background:#d6337a" aria-label="Social profile"></div>

</body>
</html>
```